Pool Screen Enclosure Building a Career Boot Camp!

Looking to Host a Boot Camp for people looking for a career or looking to change careers. We Design, Manufacture and Install Custom Pool Screen Enclosures. We have a training program to allow Non Experienced motivated people the chance at a great career that will provide a great living for them and their family. This will be a paid boot camp, week long, we provide all the initial training for them to make a transition into our business. This will be 5 days of training with a guaranteed job to start the following Monday.... This is good for both someone with no construction experience or someone with construction experience that wants to upgrade their current job.
Paid Boot Camp
transition to a full time job with great pay
Benefits include Health Insurance, Dental and Vision, 401K, we provide the tools and training.

```html
<!DOCTYPE html>
<html lang="en">
<head>
<meta charset="utf-8">
<title>Pool Screen Enclosure Career Boot Camp</title>
<link href="https://fonts.googleapis.com/css2?family=Open+Sans:wght@400;600;700;800&display=swap" rel="stylesheet">
<style>
  :root {
    --green: #0bb05a;
    --black: #000000;
    --gold: #fbb534;
    --white: #ffffff;
    --ink: #222222;
    --dark-green: #0d2a17;
    --brand-green: #4fd05a;
    --photo-main: #9ea4ab;
    --photo-main-soft: #b4b9c0;
    --photo-panel: #3f3733;
    --photo-inset-one: #a7bdd2;
    --photo-inset-two: #a3a8ad;
  }
  * { margin: 0; padding: 0; box-sizing: border-box; }
  html, body { width: 927px; height: 1200px; overflow: hidden; background: var(--white); }
  body { font-family: "Open Sans", Arial, sans-serif; color: var(--ink); }
  .flyer { position: relative; width: 927px; height: 1200px; overflow: hidden; background: var(--white); }

  .hero-green { position: absolute; left: 0; top: 50px; width: 927px; height: 664px; background: var(--green); }
  .hero-black { position: absolute; left: 580px; top: 0; width: 347px; height: 693px; background: var(--black); }

  .headline { position: absolute; left: 76px; top: 79px; color: var(--white); font-weight: 700; font-size: 26px; letter-spacing: 1.6px; white-space: nowrap; }
  .subline { position: absolute; left: 75px; top: 119px; color: var(--dark-green); font-size: 15px; white-space: nowrap; }

  .brand { position: absolute; left: 606px; top: 74px; display: flex; align-items: center; gap: 10px; }
  .brand-dot { width: 28px; height: 28px; border-radius: 50%; background: var(--brand-green); }
  .brand-name { color: var(--brand-green); font-weight: 700; font-size: 22px; white-space: nowrap; }

  .photo-main { position: absolute; left: 69px; top: 158px; width: 788px; height: 511px;
    background: linear-gradient(180deg, var(--photo-main-soft) 0%, var(--photo-main) 100%); }
  .photo-side { position: absolute; left: 69px; top: 158px; width: 145px; height: 511px; background: var(--photo-panel); }
  .side-title { position: absolute; left: 69px; top: 158px; width: 145px; height: 511px; display: flex; justify-content: center; align-items: flex-end; gap: 14px; padding-bottom: 28px; }
  .side-title span { writing-mode: vertical-rl; transform: rotate(180deg); color: var(--white); white-space: nowrap; line-height: 1; }
  .side-light { font-size: 23px; font-weight: 400; }
  .side-bold { font-size: 22.5px; font-weight: 800; letter-spacing: 0.3px; }

  .photo-inset { position: absolute; top: 562px; width: 334px; height: 165px; border: 2px solid var(--gold); }
  .photo-inset.one { left: 213px; background: var(--photo-inset-one); }
  .photo-inset.two { left: 556px; background: var(--photo-inset-two); }

  .intro { position: absolute; left: 69px; top: 746px; width: 800px; font-size: 16.2px; line-height: 21px; color: #333; }
  .intro b { font-weight: 700; color: var(--ink); }

  .details-band { position: absolute; left: 0; top: 791px; width: 927px; height: 215px; }
  .icon { position: absolute; width: 44px; height: 44px; border-radius: 50%; background: var(--gold); box-shadow: 0 3px 0 var(--green); display: flex; align-items: center; justify-content: center; }
  .detail { position: absolute; top: 886px; color: var(--white); font-size: 14.8px; line-height: 18.3px; }
  .detail em { font-style: normal; color: var(--gold); font-weight: 700; }

  .perks { position: absolute; left: 0; top: 1006px; width: 927px; height: 91px; background: var(--gold); }
  .perks ul { position: absolute; list-style: none; font-size: 15.3px; color: #1a1a1a; }
  .perks li { position: relative; padding-left: 14px; height: 27.5px; line-height: 22px; white-space: nowrap; }
  .perks li::before { content: ""; position: absolute; left: 0; top: 9px; width: 5px; height: 5px; border-radius: 50%; background: #1a1a1a; }
  .perks .tag { background: var(--black); color: var(--white); font-weight: 700; padding: 0 4px; }

  .footer { position: absolute; left: 0; top: 1097px; width: 927px; height: 103px; background: var(--green); }
  .contact { position: absolute; display: flex; align-items: center; color: var(--dark-green); font-weight: 700; white-space: nowrap; }
  .address { left: 68px; top: 1118px; font-size: 14.4px; line-height: 21px; gap: 12px; }
  .phone { left: 295px; top: 1116px; font-size: 30px; color: var(--white); letter-spacing: 1.5px; gap: 8px; }
  .email { left: 600px; top: 1118px; font-size: 15px; gap: 9px; }
  .email .at { font-size: 24px; line-height: 1; }
</style>
</head>
<body>
<div class="flyer">
  <div class="hero-green"></div>
  <div class="hero-black"></div>

  <h1 class="headline">LOOKING TO HOST A BOOT CAMP</h1>
  <p class="subline">for people looking for a career or looking to change careers.</p>

  <div class="brand">
    <div class="brand-dot"></div>
    <div class="brand-name">Shoreline Screenworks</div>
  </div>

  <div class="photo-main" role="img" aria-label="Photo: finished screened pool enclosure beside a lake"></div>
  <div class="photo-side"></div>
  <div class="side-title">
    <span class="side-light">Designing, Manufacturing and Building</span>
    <span class="side-bold">CUSTOM POOL SCREEN ENCLOSURES</span>
  </div>
  <div class="photo-inset one" role="img" aria-label="Photo: two installers fitting a panel on an enclosure roof"></div>
  <div class="photo-inset two" role="img" aria-label="Photo: installer on a ladder hanging screen inside an enclosure frame"></div>

  <p class="intro">We have <b>A TRAINING PROGRAM</b> to allow Non Experienced motivated people the <b>chance at a great career</b> that will provide a great living for them and their family.</p>

  <svg class="details-band" viewBox="0 0 927 215" preserveAspectRatio="none" aria-hidden="true">
    <polygon points="0,0 463,57 927,0 927,215 0,215" fill="#000"/>
  </svg>

  <div class="icon" style="left:146px; top:806px;">
    <svg width="24" height="20" viewBox="0 0 24 20"><rect x="1" y="4" width="22" height="15" rx="2" fill="#fff"/><rect x="3" y="1" width="14" height="5" rx="1" fill="#fff" opacity=".8"/><rect x="16" y="9" width="7" height="5" rx="1" fill="#fbb534"/></svg>
  </div>
  <div class="icon" style="left:438px; top:832px;">
    <svg width="22" height="22" viewBox="0 0 22 22"><rect x="2" y="4" width="18" height="16" rx="2" fill="none" stroke="#fff" stroke-width="2"/><rect x="2" y="4" width="18" height="4" fill="#fff"/><rect x="6" y="1" width="2" height="5" fill="#fff"/><rect x="14" y="1" width="2" height="5" fill="#fff"/><g fill="#fff"><rect x="5" y="11" width="3" height="2"/><rect x="10" y="11" width="3" height="2"/><rect x="15" y="11" width="2" height="2"/><rect x="5" y="15" width="3" height="2"/><rect x="10" y="15" width="3" height="2"/></g></svg>
  </div>
  <div class="icon" style="left:718px; top:805px;">
    <svg width="24" height="24" viewBox="0 0 24 24"><circle cx="12" cy="7" r="4" fill="#fff"/><path d="M4 20 L12 13 L20 20" fill="none" stroke="#fff" stroke-width="3" stroke-linecap="round"/></svg>
  </div>

  <p class="detail" style="left:69px; width:252px;">This will be <em>a paid boot camp</em>, week long, we provide all the initial training for them to make a transition into our business.</p>
  <p class="detail" style="left:353px; width:218px;">This will be <em>5 days</em> of training with a guaranteed job to start the <em>following Monday....</em></p>
  <p class="detail" style="left:594px; width:256px;">This is good for both someone with <em>no construction experience</em> or someone with construction experience that wants to <em>upgrade their current job</em>.</p>

  <div class="perks">
    <ul style="left:78px; top:6px;">
      <li>Paid Boot Camp</li>
      <li>Transition to a full time job with great pay</li>
      <li>Benefits include Health Insurance</li>
    </ul>
    <ul style="left:513px; top:6px;">
      <li>Dental and Vision, 401K,</li>
      <li><span class="tag">WE PROVIDE THE TOOLS AND TRAINING</span></li>
    </ul>
  </div>

  <div class="footer"></div>
  <svg style="position:absolute; left:0; top:1177px;" width="927" height="23" aria-hidden="true">
    <polygon points="203,0 724,0 738,23 189,23" fill="#fff"/>
  </svg>

  <div class="contact address">
    <svg width="20" height="30" viewBox="0 0 20 30"><path d="M10 0 C4.5 0 0 4.5 0 10 C0 17 10 30 10 30 C10 30 20 17 20 10 C20 4.5 15.5 0 10 0 Z" fill="#0d2a17"/><circle cx="10" cy="10" r="4" fill="#0bb05a"/></svg>
    <span>1420 Harbor Point Road<br>Palm Cove, FL 34990</span>
  </div>
  <div class="contact phone">
    <svg width="30" height="30" viewBox="0 0 24 24"><path d="M6.6 10.8c1.4 2.8 3.8 5.1 6.6 6.6l2.2-2.2c.3-.3.7-.4 1-.2 1.1.4 2.3.6 3.6.6.6 0 1 .4 1 1V20c0 .6-.4 1-1 1C10.6 21 3 13.4 3 4c0-.6.4-1 1-1h3.5c.6 0 1 .4 1 1 0 1.3.2 2.5.6 3.6.1.3 0 .7-.2 1L6.6 10.8z" fill="#fff"/></svg>
    <span>555-014-2290</span>
  </div>
  <div class="contact email">
    <span class="at">@</span>
    <span>hello@shorelinescreenworks.com</span>
  </div>
</div>
</body>
</html>
```